Website Performance Testing eBook for the software testing industry

Overview:
I would like an ebook/whitepaper designed. This ebook will be digital published on my website as a lead generation piece. The purpose is to give high level tips on what to look for and things to think about when working on a website performance testing project.
The ebook also demonstrates our expertise and knowledge on the topic.
Topic:
This is an ebook on software testing. Specifically, website performance testing.
About Veltrano:
Veltrano Solutions is an outsourcing development and software testing firm, and we provide expert services for application development, testing and data analytics. We extend our clients’ software testing capabilities with on-demand technical expertise. Our quality assurance resources work as part of our clients’ teams to help test applications on time and within budget.
Our model is designed to allocate the right mix of local and offshore resources in order to optimize expertise, speed and cost. We provide the ability to quickly add specialty skills to our client’s development team without them incurring long-term costs. The result is far better management of resource capacities and outcomes.
Background on our branding and previous pieces:
I have included a few of our previous ebooks and whitepapers. I like the look and feel of these pieces, however we have made updates to our brand guidelines since them, so the new brand guidelines will need to be incorporated, and I'd like to refresh/update what we have done in the past.
Refer to our website for an idea of our look and feel. This page is one of our newer sections and would be a good reference:
http://www.veltranosol.example/data-analytics/
Tone and feel:
- The look and feel should be professional, clean and polished.
- I like good use of whitespace.
- I would prefer to keep stock photography of people to a minimum. Any images should add to the content and be relevant to the content.
(Also, I uploaded some InDesign files in case you wanted to refer to those assets, but I didn't include the Links folder because they were too big. If there's anything you more you need, let me know)
Target Market(s)
Audience:
The audience is senior Quality Assurance and Software Testing professionals.
- 30-45 years old
- Technical mindset
- Interested in learning
Titles include
- QA Lead
- QA Manager
- QA Director
- Director or VP of Development
- QA Automation Engineer
Our customers are medium to large sized companies. Many are software companies, but many are also enterprises in all almost all industries.

```html
<!DOCTYPE html>
<html lang="en">
<head>
<meta charset="utf-8">
<title>Website Performance Testing eBook – Spread</title>
<link href="https://fonts.googleapis.com/css2?family=Open+Sans:ital,wght@0,400;0,600;0,700;1,400&display=swap" rel="stylesheet">
<style>
  :root{
    --bg:#d9d8d4;
    --paper:#ffffff;
    --ink:#3a3a3a;
    --muted:#6f6f6f;
    --red:#c8423a;
    --band:#d3d4d6;
    --orange:#e6a22e;
    --green:#4e9e86;
    --slate:#757575;
    --blue:#4fa3d9;
    --purple:#a88cc6;
    --cyan:#4fb0c6;
    --lime:#a9c23f;
    --charcoal:#6b6b6b;
    --dots:#9a9a9a;
  }
  *{box-sizing:border-box;margin:0;padding:0}
  html,body{width:1200px;height:804px;overflow:hidden;background:var(--bg);font-family:"Open Sans",Arial,sans-serif;color:var(--ink)}
  .spread{position:absolute;left:20px;top:12px;width:1160px;height:780px;display:flex;box-shadow:0 4px 18px rgba(0,0,0,.18)}
  .page{position:relative;width:580px;height:780px;background:var(--paper);overflow:hidden}
  .page--left{background:linear-gradient(90deg,#fff 85%,#ececec)}
  .page--right{background:linear-gradient(90deg,#ececec,#fff 15%)}

  .running-head{position:absolute;top:30px;font-size:10px;line-height:1.6;color:var(--ink)}
  .page--left .running-head{right:40px;text-align:right}
  .page--right .running-head{left:40px}
  .running-head span{display:block}
  .rule{position:absolute;top:44px;height:2px;background:var(--red)}
  .page--left .rule{left:40px;right:110px}
  .page--right .rule{left:110px;right:40px}
  .tab{position:absolute;top:36px;width:50px;height:20px;background:var(--red)}
  .page--left .tab{left:0}
  .page--right .tab{right:0}
  .tab svg{position:absolute;top:2px;width:16px;height:16px}
  .page--left .tab svg{right:4px}
  .page--right .tab svg{left:4px}

  .title{position:absolute;font-weight:400;line-height:1.1}
  .title .accent{display:block;color:var(--red)}
  .title .plain{display:block;color:var(--muted)}
  .page--left .title{left:50px;top:88px;font-size:31px}

  .body-copy{position:absolute;left:50px;top:176px;width:480px;font-size:10.5px;line-height:1.45;color:var(--ink)}
  .body-copy p{margin-bottom:10px}

  .illustration{position:absolute;left:80px;top:505px;width:420px;height:178px;border-radius:6px;
    background:radial-gradient(circle at 45% 55%,#d9574a 0 16%,transparent 17%),linear-gradient(135deg,#f3d9a6,#e8e2d6 40%,#4b6272 75%,#7fb8c0)}

  .footer-band{position:absolute;left:0;right:0;bottom:0;height:52px;background:var(--band)}
  .url{position:absolute;bottom:20px;font-size:10px;color:var(--ink)}
  .page--left .url{left:300px}
  .page--right .url{left:200px}
  .folio{position:absolute;top:692px;width:20px;height:20px;border:2px solid var(--red);border-radius:50%;font-size:10px;font-weight:700;text-align:center;line-height:16px;color:var(--ink);background:#fff}
  .page--left .folio{right:20px}
  .page--right .folio{left:20px}
  .social{position:absolute;bottom:0;width:170px;height:48px;background:var(--red);display:flex;gap:10px;align-items:center;justify-content:center}
  .page--left .social{left:0}
  .page--right .social{right:0}
  .social i{display:block;width:13px;height:13px;border-radius:2px;background:#fff;opacity:.9}

  .page--right .title{left:40px;top:72px;font-size:29px}
  .lede{position:absolute;left:40px;top:152px;font-size:11px;font-style:italic;color:var(--muted)}

  .tips{position:absolute;list-style:none;display:flex;flex-direction:column}
  .tips::before{content:"";position:absolute;left:69px;top:4px;bottom:4px;border-left:1.5px dotted var(--dots)}
  .tips--do{left:40px;top:200px;gap:16px}
  .tips--dont{left:290px;top:180px;gap:14px}

  .tip{position:relative;display:flex;align-items:flex-start}
  .tip .num{width:56px;height:20px;color:#fff;font-size:12px;font-weight:600;display:flex;align-items:center;justify-content:center;flex:none}
  .tip .dot{position:relative;width:8px;height:8px;border-radius:50%;border:1.5px solid #8a8a8a;background:#fff;margin:6px 8px 0 9px;flex:none}
  .tip .dot--solid{background:#777;border-color:#777}
  .tip p{font-size:9px;line-height:1.35;color:var(--ink)}
  .tips--do p{width:150px}
  .tips--dont p{width:170px}
</style>
</head>
<body>
<main class="spread">

  <section class="page page--left">
    <div class="tab"><svg viewBox="0 0 16 16"><path d="M5 3l6 5-6 5" fill="none" stroke="#fff" stroke-width="2"/></svg></div>
    <div class="rule"></div>
    <div class="running-head"><span>Website Performance</span><span>testing ebook</span></div>

    <h1 class="title"><span class="accent">Website Performance</span><span class="plain">Testing Approach</span></h1>

    <div class="body-copy">
      <p>When designing your web performance testing, use a logical approach that gradually narrows down on defects in design, development and deployment. Start with a clear set of objectives and measurable criteria for what your performance tests are to accomplish. Otherwise, you can waste effort testing the wrong things in the wrong places plus be unaware when the test effort is losing effectiveness.</p>
      <p>Plan to start performance testing as early as possible in your development cycle to harvest the low-hanging fruit such as major imbalances in the software’s implementation. If possible, engage developers in the early stages of testing. Get them into the habit of examining performance, load and stress results as soon as they become available, so code changes are not delayed and subsequent testing is tweaked effectively with developer input.</p>
      <p>To quick-start your testing effort, it helps to focus your testing and optimization efforts on the most-used or high-impact pages based on the percentage of traffic they receive, which you can determine using analysis tools or examining logs. This enables more efficient use of testing resources while deferring changes for rarely visited pages with minor impact on the customer experience.</p>
      <p>Finally, regularly review the following do’s and don’ts of website performance testing, especially with regard to cloud-based testing. This will help ensure you are receiving the full benefits of the cloud and that your testing aligns more closely to the conditions of your site when it goes live.</p>
    </div>

    <div class="illustration" role="img" aria-label="Flat illustration of performance testing tools: stopwatch, gauge, laptop with rising line chart, browser windows, tablet pie chart, magnifying glass and light bulb"></div>

    <div class="folio">4</div>
    <div class="footer-band"></div>
    <div class="url">www.veltranosol.example</div>
    <div class="social"><i></i><i></i><i></i><i></i></div>
  </section>

  <section class="page page--right">
    <div class="tab"><svg viewBox="0 0 16 16"><path d="M11 3l-6 5 6 5" fill="none" stroke="#fff" stroke-width="2"/></svg></div>
    <div class="rule"></div>
    <div class="running-head"><span>Website Performance</span><span>testing ebook</span></div>

    <h2 class="title"><span class="accent">The Do’s and Don’ts of</span><span class="plain">Website Performance Testing</span></h2>
    <p class="lede">When it is time to implement the test plan, avoid common strategic and tactical pitfalls:</p>

    <ol class="tips tips--do">
      <li class="tip"><span class="num" style="background:var(--red)">01</span><span class="dot dot--solid"></span><p>Do keep your in-house test infrastructure up-to-date even if you use cloud-based testing. It is your baseline environment for isolating cloud-based testing side-effects, which will drastically reduce the time for root cause analysis for many defects.</p></li>
      <li class="tip"><span class="num" style="background:var(--orange)">02</span><span class="dot"></span><p>Do use your live site, if one exists, to guide load and stress testing parameters on the developing site. For example, an initial test load might be the number of actual peak-hours orders multiplied by your expected growth rate plus 20 percent overhead.</p></li>
      <li class="tip"><span class="num" style="background:var(--green)">03</span><span class="dot"></span><p>Do track both client and server-side traffic during non-peak and peak performance testing to determine ratios between traffic and processing activities, which often discovers imbalances.</p></li>
      <li class="tip"><span class="num" style="background:var(--slate)">04</span><span class="dot"></span><p>Do test as many pages and combinations of page traversals as possible. Measure single page and page combination load times down to the component level.</p></li>
      <li class="tip"><span class="num" style="background:var(--blue)">05</span><span class="dot"></span><p>Do pay attention to which pages or activities are consuming an inordinate amount of time relative to other areas of the website. This helps optimize use of your test and repair resources.</p></li>
    </ol>

    <ol class="tips tips--dont" start="6">
      <li class="tip"><span class="num" style="background:var(--red)">06</span><span class="dot"></span><p>Do distribute generated loads geographically and by network segment.</p></li>
      <li class="tip"><span class="num" style="background:var(--purple)">07</span><span class="dot"></span><p>Don’t ignore the dependency between page load times and user volume capacity. Measure both aspects at each stage of testing.</p></li>
      <li class="tip"><span class="num" style="background:var(--cyan)">08</span><span class="dot"></span><p>Don’t forget to process live web traffic logs to collect statistics on the types and volume of requests coming into your site so you can optimize load testing to reflect that reality.</p></li>
      <li class="tip"><span class="num" style="background:var(--red)">09</span><span class="dot"></span><p>Don’t run your load generation on the same cloud as your website to avoid contamination of test metrics.</p></li>
      <li class="tip"><span class="num" style="background:var(--lime)">10</span><span class="dot"></span><p>Don’t assume that cloud testing is intrinsically less expensive than running on in-house infrastructure. In other words, keep your eye on the “meter.”</p></li>
      <li class="tip"><span class="num" style="background:var(--charcoal)">11</span><span class="dot dot--solid"></span><p>Don’t rely on a single cloud vendor as vendors’ distinctive functional and operational characteristics may affect test results.</p></li>
    </ol>

    <div class="folio">5</div>
    <div class="footer-band"></div>
    <div class="url">www.veltranosol.example</div>
    <div class="social"><i></i><i></i><i></i><i></i></div>
  </section>

</main>
</body>
</html>
```